Develop website for Cloud Security Startup

Looking for a logo that conveys the outsourced security and management of clients data, systems and development in Tessora, Kfn and Brintel with an emphasis on security and compliance

Target Market(s)

Companies looking for professional services IT firm

Coding

Coded - Design and coding required

Number of Pages Required

5+ page

Font styles to use
Sans Serif

Colors
0455a3
33a6d7

Requirements
Must have
• Landing Page
- Help me get started

Move to the cloud safely
- Benefits of Cloud

What we do
- Cloud Adoption
- Managed Services
- Optimise

Resources
- News
- Resources
- Events
- Webinars
- Not for profit
- Case Studies
- Support Button
- Incident Button

Company
- About Us
- Why Vorselith?
- Acreditations
- Halvendor Tessora Partner
- Net Promoter Score
- Careers
- Contact Us

Contact Us

```html
<!DOCTYPE html>
<html lang="en">
<head>
<meta charset="utf-8">
<title>Vorselith – Effective Technology Management</title>
<link href="https://fonts.googleapis.com/css2?family=Montserrat:wght@500;600;700;800&family=Arimo:wght@400;700&display=swap" rel="stylesheet">
<style>
:root{
  --brand-dark:#0455a3;
  --brand-light:#33a6d7;
  --navy:#0b3f86;
  --ink:#1f1f1f;
  --body:#5a5a5a;
  --white:#ffffff;
  --line:#d3d3d3;
}
*{box-sizing:border-box;margin:0;padding:0}
html,body{width:1200px;height:4029px;overflow:hidden;background:var(--white)}
body{font-family:"Arimo",Arial,sans-serif;color:var(--body);position:relative}
.page{position:relative;width:1200px;height:4029px;overflow:hidden}
.abs{position:absolute}
.heading{font-family:"Montserrat",Arial,sans-serif;font-weight:700;color:var(--ink);letter-spacing:.5px}

/* hero */
.hero-photo{left:0;top:0;width:1200px;height:730px;background:linear-gradient(120deg,#6f7f92 0%,#b8c3cf 35%,#d9dfe4 55%,#8e9aa8 80%,#5f6c7c 100%)}
.hero-shape{left:0;top:0}
.brand{left:110px;top:40px;display:flex;align-items:center;gap:10px}
.brand-dot{width:30px;height:30px;border-radius:50%;background:var(--brand-dark)}
.brand-name{font-family:"Montserrat",sans-serif;font-weight:700;font-size:30px;color:var(--brand-dark);letter-spacing:1px}
.nav a{font-family:"Montserrat",sans-serif;font-weight:600;font-size:14px;color:#2a2a2a;text-decoration:none;position:absolute;white-space:nowrap}
.nav a.active{color:var(--brand-dark)}
.nav-tick{left:411px;top:20px}
.nav-btn{top:25px;width:38px;height:38px;border:2px solid var(--brand-dark);border-radius:50%;display:flex;align-items:center;justify-content:center}
.welcome{left:313px;top:208px;width:572px;height:266px;background:rgba(70,76,86,.72);text-align:center;color:var(--white)}
.welcome-small{font-family:"Montserrat",sans-serif;font-weight:600;font-size:22px;margin-top:44px;letter-spacing:1px}
.welcome-big{font-family:"Montserrat",sans-serif;font-weight:800;font-size:76px;line-height:84px;letter-spacing:1px}
.btn{display:inline-flex;align-items:center;justify-content:center;border-radius:24px;color:var(--white);font-family:"Montserrat",sans-serif;font-weight:700;font-size:14px;background:linear-gradient(90deg,var(--brand-dark),var(--brand-light));white-space:nowrap}
.welcome .btn{width:226px;height:41px;margin-top:8px}
.slider-arrow{width:46px;height:46px;border-radius:50%;background:#1d1d1d;color:#fff;display:flex;align-items:center;justify-content:center;font-size:20px;top:334px}
.dots{left:568px;top:581px;display:flex;gap:5px}
.dots span{width:12px;height:12px;border-radius:50%;background:#fff}
.dots span.on{background:var(--brand-dark)}

/* what we do */
.section-icon{width:52px;height:52px;border-radius:50%;background:#dbe9f6;display:flex;align-items:center;justify-content:center}
.title-center{left:0;width:1200px;text-align:center;font-size:35px}
.lead{left:260px;width:680px;text-align:center;font-size:14px;line-height:22px}
.service{width:316px;height:316px;border-radius:50%;border:3px solid #d6d6d6;text-align:center;overflow:hidden;background:#fff}
.service.featured{border-color:var(--brand-dark);background:linear-gradient(180deg,var(--brand-light),var(--brand-dark));color:#fff}
.service h3{font-family:"Arimo",sans-serif;font-weight:700;font-size:19px;color:var(--brand-dark);margin-top:10px}
.service.featured h3{color:#fff}
.service p{font-size:14px;line-height:22px;width:250px;margin:12px auto 0}
.service-icon{margin-top:24px}
.service-go{position:absolute;left:50%;bottom:-46px;transform:translateX(-50%);width:92px;height:92px;border-radius:50%;background:var(--brand-dark);display:flex;justify-content:center;padding-top:16px}
.service.featured .service-go{background:#fff}

/* benefits */
.benefits{left:0;top:0}
.benefit-title{font-family:"Arimo",sans-serif;font-weight:700;font-size:17px;color:#fff}
.benefit-text{font-size:13px;line-height:21px;color:#e7f1fb;margin-top:6px;width:220px}
.benefit.left{text-align:right}
.benefit.left .benefit-text{margin-left:auto}
.benefit-icon{width:80px;height:80px;border-radius:50%;background:#fff;display:flex;align-items:center;justify-content:center}
.core{left:421px;top:1674px;width:360px;height:360px;border-radius:50%;background:radial-gradient(circle,#ffffff 60%,#e3e8ee 100%);text-align:center}
.core-name{font-family:"Montserrat",sans-serif;font-weight:700;font-size:44px;color:var(--brand-dark);margin-top:148px}
.core-note{font-size:9px;color:#555;margin-top:10px}

/* overview */
.overview-photo{left:156px;top:2378px;width:396px;height:383px;border-radius:50%;background:linear-gradient(135deg,#4b5a6d,#a8b1bc 55%,#8a3a3f)}
.overview-title{left:601px;top:2368px;font-size:36px}
.overview-text{left:602px;top:2425px;width:478px;font-size:13.4px;line-height:22.3px}
.overview .btn{left:604px;top:2711px;width:166px;height:43px;position:absolute}

/* news */
.news-card{top:0;width:320px;height:3400px}
.news-photo{top:2922px;left:2px;width:311px;height:202px}
.news-date{left:0;top:3151px;width:300px;font-size:13px;color:var(--brand-dark);white-space:nowrap}
.news-head{left:0;top:3184px;width:320px;font-weight:700;font-size:18px;color:var(--ink);white-space:nowrap}
.news-text{left:0;top:3214px;width:310px;font-size:13px;line-height:26px;color:#6b6b6b}
.news-more{left:0;top:3284px;width:220px;font-size:14px;color:var(--brand-dark);text-decoration:underline;white-space:nowrap}
.news-arrow{top:3125px;font-size:44px;color:#8a8a8a;font-family:"Arimo",sans-serif}

/* footer */
.foot-title{font-family:"Montserrat",sans-serif;font-weight:700;font-size:18px;color:#fff;white-space:nowrap}
.field{height:38px;background:#fff;font-size:13px;color:#777;padding:12px 18px}
.links li{list-style:none;font-size:15px;color:#fff;height:30px}
.links li::before{content:"»";color:var(--brand-light);margin-right:10px}
.contact-row{font-size:15px;color:#fff;line-height:24px;display:flex;gap:14px}
.social{width:30px;height:30px;border-radius:50%}
.copyright{left:0;width:1200px;top:3975px;text-align:center;font-size:15px;color:#fff}
</style>
</head>
<body>
<div class="page">

  <!-- hero -->
  <div class="abs hero-photo" role="img" aria-label="Photo of an IT team working together in a bright modern office"></div>
  <svg class="abs hero-shape" width="1200" height="740" viewBox="0 0 1200 740">
    <polygon points="0,568 297,725 1200,562 1200,740 0,740" fill="#ffffff"/>
    <polygon points="150,648 297,727 1200,562 1200,582 297,742" fill="#0b3f86"/>
  </svg>

  <div class="abs brand"><span class="brand-dot"></span><span class="brand-name">VORSELITH</span></div>
  <nav class="abs nav" style="left:0;top:37px">
    <a class="active" style="left:393px">HOME</a>
    <a style="left:478px">WHAT WE DO</a>
    <a style="left:615px">RESOURCES</a>
    <a style="left:748px">COMPANY</a>
    <a style="left:862px">CONTACT US</a>
  </nav>
  <svg class="abs nav-tick" width="14" height="12" viewBox="0 0 14 12"><path d="M2 6l4 4 7-8" stroke="#0455a3" stroke-width="2.5" fill="none"/></svg>
  <div class="abs nav-btn" style="left:974px">
    <svg width="16" height="16" viewBox="0 0 16 16"><circle cx="7" cy="7" r="5" stroke="#0455a3" stroke-width="2" fill="none"/><path d="M11 11l4 4" stroke="#0455a3" stroke-width="2"/></svg>
  </div>
  <div class="abs nav-btn" style="left:1018px">
    <svg width="16" height="16" viewBox="0 0 16 16"><circle cx="8" cy="5" r="3.5" fill="#0455a3"/><path d="M2 15c0-4 3-6 6-6s6 2 6 6z" fill="#0455a3"/></svg>
  </div>

  <div class="abs welcome">
    <div class="welcome-small">WELCOME TO</div>
    <div class="welcome-big">VORSELITH</div>
    <span class="btn">HELP ME GET STARTED</span>
  </div>
  <div class="abs slider-arrow" style="left:30px">‹</div>
  <div class="abs slider-arrow" style="left:1122px">›</div>
  <div class="abs dots"><span></span><span class="on"></span><span></span><span></span></div>

  <!-- what we do -->
  <div class="abs section-icon" style="left:574px;top:756px">
    <svg width="30" height="30" viewBox="0 0 30 30"><circle cx="15" cy="15" r="6" stroke="#0455a3" stroke-width="2.5" fill="none"/><circle cx="15" cy="15" r="11" stroke="#33a6d7" stroke-width="2.5" stroke-dasharray="4 3" fill="none"/></svg>
  </div>
  <h2 class="abs heading title-center" style="top:818px">WHAT WE DO</h2>
  <p class="abs lead" style="top:873px">Lorem ipsum dolor sit amet, consectetur adipiscing elit, sed do eiusmod tempor incididunt ut labore et dolore magna aliqua. Ut enim ad minim veniam, quis nostrud</p>

  <div class="abs service" style="left:110px;top:948px">
    <svg class="service-icon" width="76" height="76" viewBox="0 0 76 76"><path d="M18 46a12 12 0 0 1 2-24 18 18 0 0 1 34 2 11 11 0 0 1 2 22z" stroke="#0455a3" stroke-width="2.5" fill="none"/><path d="M28 46v14M38 46v20M48 46v14" stroke="#33a6d7" stroke-width="2.5"/><circle cx="28" cy="62" r="3" fill="#33a6d7"/><circle cx="38" cy="68" r="3" fill="#33a6d7"/><circle cx="48" cy="62" r="3" fill="#33a6d7"/></svg>
    <h3>Cloud Adoption</h3>
    <p>Lorem ipsum dolor sit amet, consectetur adipiscing elit, sed do eiusmod tempor incididunt ut labore et dolore magna aliqua. Ut enim ad minim veniam, quis nostrud</p>
    <div class="service-go"><svg width="18" height="18" viewBox="0 0 18 18"><path d="M3 3l6 6-6 6M9 3l6 6-6 6" stroke="#fff" stroke-width="2.2" fill="none"/></svg></div>
  </div>
  <div class="abs service featured" style="left:441px;top:948px">
    <svg class="service-icon" width="76" height="76" viewBox="0 0 76 76"><circle cx="38" cy="38" r="24" stroke="#fff" stroke-width="2.5" stroke-dasharray="8 4" fill="none"/><circle cx="38" cy="38" r="14" stroke="#fff" stroke-width="2.5" fill="none"/><path d="M24 52a16 10 0 0 1 28 0" stroke="#fff" stroke-width="2.5" fill="none"/></svg>
    <h3>Managed Services</h3>
    <p>Lorem ipsum dolor sit amet, consectetur adipiscing elit, sed do eiusmod tempor incididunt ut labore et dolore magna aliqua. Ut enim ad minim veniam, quis nostrud</p>
    <div class="service-go"><svg width="18" height="18" viewBox="0 0 18 18"><path d="M3 3l6 6-6 6M9 3l6 6-6 6" stroke="#0455a3" stroke-width="2.2" fill="none"/></svg></div>
  </div>
  <div class="abs service" style="left:773px;top:948px">
    <svg class="service-icon" width="76" height="76" viewBox="0 0 76 76"><circle cx="38" cy="38" r="26" stroke="#0455a3" stroke-width="2.5" stroke-dasharray="9 4" fill="none"/><circle cx="38" cy="38" r="16" stroke="#33a6d7" stroke-width="2.5" fill="none"/><path d="M32 33l-5 5 5 5M44 33l5 5-5 5M40 31l-4 14" stroke="#0455a3" stroke-width="2.2" fill="none"/></svg>
    <h3>Optimise</h3>
    <p>Lorem ipsum dolor sit amet, consectetur adipiscing elit, sed do eiusmod tempor incididunt ut labore et dolore magna aliqua. Ut enim ad minim veniam, quis nostrud</p>
    <div class="service-go"><svg width="18" height="18" viewBox="0 0 18 18"><path d="M3 3l6 6-6 6M9 3l6 6-6 6" stroke="#fff" stroke-width="2.2" fill="none"/></svg></div>
  </div>

  <!-- benefits -->
  <svg class="abs benefits" width="1200" height="2300" viewBox="0 0 1200 2300">
    <defs>
      <linearGradient id="benefitsFill" x1="0" y1="0" x2="1" y2="1">
        <stop offset="0" stop-color="#0455a3"/>
        <stop offset=".6" stop-color="#2a86c9"/>
        <stop offset="1" stop-color="#1f6fb8"/>
      </linearGradient>
    </defs>
    <polygon points="0,1518 900,1362 1200,1464 1200,1474 900,1372 0,1528" fill="#cfe2f3"/>
    <polygon points="0,1528 900,1369 1200,1471 1200,2112 297,2272 0,2115" fill="url(#benefitsFill)"/>
    <polygon points="0,2115 297,2272 1200,2112 1200,2124 297,2286 0,2125" fill="#0b3f86"/>
    <path d="M511 1665 A214 214 0 0 0 511 2043" stroke="#fff" stroke-width="5" fill="none"/>
    <path d="M691 1665 A214 214 0 0 1 691 2043" stroke="#fff" stroke-width="5" fill="none"/>
    <g fill="#33a6d7" stroke="#fff" stroke-width="3">
      <circle cx="469" cy="1682" r="13"/><circle cx="386" cy="1854" r="13"/><circle cx="469" cy="2026" r="13"/>
      <circle cx="727" cy="1682" r="13"/><circle cx="812" cy="1854" r="13"/><circle cx="727" cy="2026" r="13"/>
    </g>
  </svg>
  <div class="abs section-icon" style="left:574px;top:1476px;background:#1d6fb8;border:2px solid #cfe2f3">
    <svg width="30" height="30" viewBox="0 0 30 30"><rect x="5" y="7" width="20" height="16" rx="2" stroke="#fff" stroke-width="2" fill="none"/><path d="M9 18a4 4 0 0 1 2-7 5 5 0 0 1 9 1 3 3 0 0 1 0 6z" stroke="#fff" stroke-width="1.8" fill="none"/></svg>
  </div>
  <h2 class="abs heading title-center" style="top:1538px;color:#fff">BENEFITS OF CLOUD</h2>

  <div class="abs core">
    <div class="core-name">VORSELITH</div>
    <div class="core-note">Secure cloud services for growing teams</div>
  </div>

  <div class="abs benefit left" style="left:99px;top:1638px;width:220px"><div class="benefit-title">Nemo enim ipsaam</div><div class="benefit-text">Sed ut perspiciatis unde omnis iste natus error sit voluptatem accusant ium doloremque laudantium</div></div>
  <div class="abs benefit left" style="left:47px;top:1810px;width:220px"><div class="benefit-title">Nemo enim ipsaam</div><div class="benefit-text">Sed ut perspiciatis unde omnis iste natus error sit voluptatem accusant ium doloremque laudantium</div></div>
  <div class="abs benefit left" style="left:99px;top:1981px;width:220px"><div class="benefit-title">Nemo enim ipsaam</div><div class="benefit-text">Sed ut perspiciatis unde omnis iste natus error sit voluptatem accusant ium doloremque laudantium</div></div>
  <div class="abs benefit" style="left:879px;top:1638px;width:220px"><div class="benefit-title">Nemo enim ipsaam</div><div class="benefit-text">Sed ut perspiciatis unde omnis iste natus error sit voluptatem accusant ium doloremque laudantium</div></div>
  <div class="abs benefit" style="left:931px;top:1810px;width:220px"><div class="benefit-title">Nemo enim ipsaam</div><div class="benefit-text">Sed ut perspiciatis unde omnis iste natus error sit voluptatem accusant ium doloremque laudantium</div></div>
  <div class="abs benefit" style="left:879px;top:1981px;width:220px"><div class="benefit-title">Nemo enim ipsaam</div><div class="benefit-text">Sed ut perspiciatis unde omnis iste natus error sit voluptatem accusant ium doloremque laudantium</div></div>

  <div class="abs benefit-icon" style="left:340px;top:1642px"><svg width="44" height="44" viewBox="0 0 44 44"><rect x="10" y="20" width="24" height="18" rx="3" stroke="#0455a3" stroke-width="2.2" fill="none"/><path d="M15 20v-6a7 7 0 0 1 14 0v6" stroke="#0455a3" stroke-width="2.2" fill="none"/><circle cx="22" cy="29" r="3" fill="#33a6d7"/></svg></div>
  <div class="abs benefit-icon" style="left:289px;top:1817px"><svg width="44" height="44" viewBox="0 0 44 44"><circle cx="16" cy="18" r="8" stroke="#0455a3" stroke-width="2.2" fill="none"/><path d="M22 24l14 14M30 32l4-4" stroke="#33a6d7" stroke-width="2.2"/></svg></div>
  <div class="abs benefit-icon" style="left:340px;top:1986px"><svg width="44" height="44" viewBox="0 0 44 44"><path d="M12 30a8 8 0 0 1 2-15 11 11 0 0 1 20 2 7 7 0 0 1 0 13z" stroke="#0455a3" stroke-width="2.2" fill="none"/><rect x="17" y="24" width="10" height="8" rx="1" fill="#33a6d7"/></svg></div>
  <div class="abs benefit-icon" style="left:778px;top:1642px"><svg width="44" height="44" viewBox="0 0 44 44"><circle cx="22" cy="16" r="6" stroke="#0455a3" stroke-width="2.2" fill="none"/><circle cx="22" cy="16" r="11" stroke="#0455a3" stroke-width="2" stroke-dasharray="4 3" fill="none"/><path d="M8 38l8-8h12" stroke="#33a6d7" stroke-width="2.2" fill="none"/></svg></div>
  <div class="abs benefit-icon" style="left:830px;top:1817px"><svg width="44" height="44" viewBox="0 0 44 44"><path d="M22 6l13 5v10c0 9-6 15-13 17-7-2-13-8-13-17V11z" stroke="#0455a3" stroke-width="2.2" fill="none"/><path d="M16 22l5 5 8-9" stroke="#33a6d7" stroke-width="2.2" fill="none"/></svg></div>
  <div class="abs benefit-icon" style="left:778px;top:1986px"><svg width="44" height="44" viewBox="0 0 44 44"><rect x="13" y="18" width="18" height="14" rx="2" stroke="#0455a3" stroke-width="2.2" fill="none"/><path d="M17 18v-4a5 5 0 0 1 10 0v4M6 38h32" stroke="#33a6d7" stroke-width="2.2" fill="none"/></svg></div>

  <!-- company overview -->
  <section class="overview">
    <div class="abs overview-photo" role="img" aria-label="Photo of developers working at computers in an office"></div>
    <h2 class="abs heading overview-title">COMPANY OVERVIEW</h2>
    <p class="abs overview-text">Lorem ipsum dolor sit amet, consectetur adipiscing elit, sed do eiusmod tempor incididunt ut labore et dolore magna aliqua. Ut enim ad minim veniam, quis nostrud exercitation ullamco laboris nisi ut aliquip ex ea commodo consequat. Duis aute irure dolor in reprehenderit in voluptate velit esse cillum dolore eu fugiat nulla pariatur. Excepteur sint occaecat cupidatat non proident, sunt in culpa qui officia deserunt mollit anim id est laborum Lorem ipsum dolor sit amet, consectetur adipiscing elit, sed do eiusmod tempor incididunt ut labore et dolore magna aliqua. Ut enim ad minim veniam, quis nostrud exercitation ullamco laboris nisi ut aliquip ex ea commodo consequat. Duis aute irure dolor in reprehenderit in voluptate velit esse cillum dolore eu fugiat nulla pariatur. Excepteur sint occaecat cupidatat non proident, sunt in culpa qui officia deserunt mollit anim id est laborum.</p>
    <span class="btn">READ MORE ➔</span>
  </section>

  <!-- latest news -->
  <h2 class="abs heading title-center" style="top:2848px">LATEST NEWS</h2>
  <div class="abs news-arrow" style="left:44px">‹</div>
  <div class="abs news-arrow" style="left:1130px">›</div>

  <article class="abs news-card" style="left:109px">
    <div class="abs news-photo" style="background:linear-gradient(135deg,#d8dde3,#b9a89a 50%,#eef0f2)" role="img" aria-label="Photo of two colleagues reviewing a laptop"></div>
    <div class="abs news-date">▦ January 30,2020</div>
    <div class="abs news-head">Lorem ipsum dolor sit amet</div>
    <div class="abs news-text">Lorem ipsum dolor sit amet, consectetur adipi scing elit, sed do eiusmod tempor</div>
    <div class="abs news-more">CONTINUE READING ➔</div>
  </article>
  <article class="abs news-card" style="left:442px">
    <div class="abs news-photo" style="background:linear-gradient(135deg,#5c5a58,#9a968f 50%,#3d3d3f)" role="img" aria-label="Photo of a desktop monitor showing code in an office"></div>
    <div class="abs news-date">▦ January 30,2020</div>
    <div class="abs news-head">Lorem ipsum dolor sit amet</div>
    <div class="abs news-text">Lorem ipsum dolor sit amet, consectetur adipi scing elit, sed do eiusmod tempor</div>
    <div class="abs news-more">CONTINUE READING ➔</div>
  </article>
  <article class="abs news-card" style="left:775px">
    <div class="abs news-photo" style="background:linear-gradient(135deg,#2b3036,#8d7a62 55%,#c49a6c)" role="img" aria-label="Photo of a developer at a desk with laptop and monitors"></div>
    <div class="abs news-date">▦ January 30,2020</div>
    <div class="abs news-head">Lorem ipsum dolor sit amet</div>
    <div class="abs news-text">Lorem ipsum dolor sit amet, consectetur adipi scing elit, sed do eiusmod tempor</div>
    <div class="abs news-more">CONTINUE READING ➔</div>
  </article>

  <!-- footer -->
  <svg class="abs" style="left:0;top:3390px" width="1200" height="640" viewBox="0 0 1200 640">
    <defs>
      <linearGradient id="footFill" x1="0" y1="0" x2="1" y2="1">
        <stop offset="0" stop-color="#0b3f86"/><stop offset=".5" stop-color="#1b5fae"/><stop offset="1" stop-color="#0a3c80"/>
      </linearGradient>
    </defs>
    <polygon points="0,170 900,8 1200,108 1200,118 900,18 0,180" fill="#cfe2f3"/>
    <polygon points="0,180 900,14 1200,114 1200,640 0,640" fill="url(#footFill)"/>
    <line x1="111" y1="565" x2="1087" y2="565" stroke="#4f7fbf" stroke-width="1"/>
  </svg>

  <h3 class="abs foot-title" style="left:111px;top:3634px">GET IN TOUCH</h3>
  <div class="abs field" style="left:111px;top:3683px;width:235px">First Name</div>
  <div class="abs field" style="left:354px;top:3683px;width:234px">Last Name</div>
  <div class="abs field" style="left:111px;top:3731px;width:235px">Email</div>
  <div class="abs field" style="left:354px;top:3731px;width:234px">phone number</div>
  <div class="abs field" style="left:111px;top:3781px;width:477px;height:74px">Message</div>
  <span class="abs btn" style="left:111px;top:3875px;width:133px;height:43px;background:var(--brand-light)">SUBMIT</span>

  <h3 class="abs foot-title" style="left:649px;top:3634px">QUICK LINKS</h3>
  <ul class="abs links" style="left:649px;top:3672px">
    <li>Home</li><li>Benefits</li><li>What we do</li><li>Resources</li><li>Company</li><li>Contact Us</li>
  </ul>

  <h3 class="abs foot-title" style="left:846px;top:3634px">CONTACT US</h3>
  <div class="abs contact-row" style="left:850px;top:3672px;width:240px">
    <svg width="12" height="16" viewBox="0 0 12 16" style="margin-top:4px;flex:none"><path d="M6 1a5 5 0 0 1 5 5c0 4-5 9-5 9S1 10 1 6a5 5 0 0 1 5-5z" fill="#33a6d7"/><circle cx="6" cy="6" r="2" fill="#0b3f86"/></svg>
    <span>123,Lorem ipsum dolor sit amet, consectetur adipiscing elit sed do eiusmod</span>
  </div>
  <div class="abs contact-row" style="left:848px;top:3760px">
    <svg width="12" height="16" viewBox="0 0 12 16" style="margin-top:4px"><rect x="1.5" y="1" width="9" height="14" rx="1.5" stroke="#33a6d7" stroke-width="1.6" fill="none"/></svg>
    <span>+1 555 010 2040</span>
  </div>
  <div class="abs contact-row" style="left:846px;top:3800px">
    <svg width="16" height="12" viewBox="0 0 16 12" style="margin-top:6px"><rect x="1" y="1" width="14" height="10" stroke="#33a6d7" stroke-width="1.5" fill="none"/><path d="M1 1l7 6 7-6" stroke="#33a6d7" stroke-width="1.5" fill="none"/></svg>
    <span>hello@vorselith.example</span>
  </div>

  <h3 class="abs foot-title" style="left:649px;top:3886px">STAY CONNECTED :</h3>
  <span class="abs social" style="left:851px;top:3882px;background:#3b5bb5"></span>
  <span class="abs social" style="left:889px;top:3882px;background:#d12a8a"></span>

  <p class="abs copyright">© 2021 Vorselith Ltd &nbsp;| All Rights Reserved | Terms and Conditions</p>
</div>
</body>
</html>
```